Wine Labels for new product to attract Millenial consumers

SipRoam Design Brief
1. Intro:
Marrabel Cellars is a 120 year old family owned Australian wine company renowned for producing traditional premium quality wines. This project is aimed at breaking through this perception of Marrabel to show main stream Australian retailers that we can be innovative and relevant and that we know who their millennial shoppers are and we know how to attract their attention. This needs to be achieved through the combination of innovative and clever design paired with a product that challenges conventional Australian wine philosophies and appeals to those wine drinkers seeking authentic and alternative wine experiences.
2. Feelings:
This new wine should evoke a new set of feelings in retailers that they don’t usually associate with Marrabel Cellars. Retailers should feel excited, challenged and impressed by our knowledge of the millennial demographic. The packaging should make the shopper feel surprised, curious, cool, aspirational, understood, adventurous, individual, fashionable, progressive and engaged. It also needs to evoke a sense of the occasion it should be consumed in, with food and friends in a fun environment and evoke a sense of conviviality and a desire for shared social interaction.
3. Look + Feel:
It shouldn’t look or feel like anything Marrabel Cellars is known for and has done before. It should not carry our branding or logo, this should be a standalone product range. It should feel modern, cool, clever and hip. It should feel real, authentic, artisanal and most of all it should challenge the traditional visual discourse of wine as bored, tired, stiff and conservative. The design should be respected piece of art in its own right. It should make the shopper feel like getting a few friends around for dinner and drinks.
4. Brand Position:
This product range needs to challenge the existing brand positioning of Marrabel Cellars. It should clearly target the millennial demographic and the hipster sub culture who are being lured into new alcohol categories by cool design and positioning. “Exposed to a barrage of drinks offerings, the report found that wine is in danger of losing Generation Y to other more engaging drinks categories such as beer, cider and spirits ……. With 18-25 year olds accounting for 25% of the wine drinking population, Millennials represent an important sector of the wine market, thus keeping their attention and interest should remain a priority for wine brands.” Grape Insight Review. “…. Wine is becoming increasingly cool with the influencers and trend setters of a whole new generation.” Pour Journal.
5. Needs:
2 wine labels, one white and one red, but linked by design. Should fit a 500 ml glass bottle and design should be able to carry over to some innovative packaging into small lots of 4 or 6 like beer. For the purpose of design use the name SipRoam White and SipRoam Red. Relating the wine to food and how it should be consumed is important as this needs to be seen as a lifestyle accessory to food to combat the anti-alcohol lobby and the socially acceptable practise of eating and drinking together as part of a social experience. An area for approximately 200 words of mandatory information and declarations needs to be provided.

https://www.examplepins.test/MarrabelCellars/siproam-moodboard/

Full brief in project description

Requirements
Must have
• Full brief in project description
Nice to have
Should not have

```html
<!DOCTYPE html>
<html lang="en">
<head>
<meta charset="utf-8">
<title>SipRoam Red &amp; White Labels</title>
<link rel="stylesheet" href="https://fonts.googleapis.com/css2?family=Quicksand:wght@300;400&family=Dosis:wght@400;500&display=swap">
<style>
  :root {
    --canvas-bg: #efe9e2;
    --label-black: #1e1d1f;
    --label-rule: #8a8a8c;
    --label-text: #f2f2f2;
    --red-deep: #6e2a17;
    --red-mid: #a8401f;
    --red-warm: #c5532a;
    --teal-deep: #123f3f;
    --teal-mid: #1f6b66;
    --teal-light: #3c8c83;
  }
  * { margin: 0; padding: 0; box-sizing: border-box; }
  html, body { width: 1200px; height: 1000px; overflow: hidden; }
  body {
    background: var(--canvas-bg);
    position: relative;
    font-family: "Dosis", sans-serif;
  }
  .label {
    position: absolute;
    top: 118px;
    width: 240px;
    height: 764px;
    background: var(--label-black);
    color: var(--label-text);
  }
  .label--red { left: 300px; }
  .label--white { left: 660px; }

  .label__art {
    position: absolute;
    left: 22px; top: 22px;
    width: 196px; height: 364px;
    overflow: hidden;
  }
  .label__art-fill {
    position: absolute;
    inset: 0;
  }
  .label--red .label__art-fill,
  .label--red .label__band {
    background: linear-gradient(160deg, var(--red-deep) 0%, var(--red-mid) 40%, var(--red-warm) 60%, var(--red-deep) 100%);
  }
  .label--white .label__art-fill,
  .label--white .label__band {
    background: linear-gradient(160deg, var(--teal-mid) 0%, var(--teal-deep) 35%, var(--teal-light) 60%, var(--teal-deep) 100%);
  }
  .label__name {
    position: absolute;
    left: 10px;
    bottom: 26px;
    writing-mode: vertical-rl;
    transform: rotate(180deg);
    white-space: nowrap;
    font-family: "Quicksand", sans-serif;
    font-weight: 300;
    font-size: 40px;
    letter-spacing: 2px;
    line-height: 1;
    color: var(--label-text);
  }
  .label__rule {
    position: absolute;
    left: 20px; right: 20px;
    height: 2px;
    background: var(--label-rule);
  }
  .label__rule--top { top: 404px; }
  .label__rule--bottom { top: 488px; }
  .label__vintage {
    position: absolute;
    top: 426px; left: 0; right: 0;
    text-align: center;
    font-size: 30px;
    font-weight: 400;
    line-height: 40px;
    letter-spacing: 1px;
  }
  .label__type,
  .label__volume {
    position: absolute;
    left: 0; right: 0;
    text-align: center;
    font-size: 21px;
    line-height: 28px;
    letter-spacing: 1.5px;
  }
  .label__type { top: 518px; }
  .label__volume { top: 556px; }
  .label__abv {
    position: absolute;
    top: 636px; left: 0; right: 0;
    text-align: center;
    font-size: 20px;
    line-height: 28px;
    letter-spacing: 0.5px;
  }
  .label__band {
    position: absolute;
    left: 22px; right: 22px;
    top: 696px;
    height: 36px;
  }
</style>
</head>
<body>
  <section class="label label--red">
    <div class="label__art">
      <div class="label__art-fill" role="img" aria-label="Abstract painted canvas texture in rust red and ochre tones"></div>
      <h1 class="label__name">SipRoam</h1>
    </div>
    <div class="label__rule label__rule--top"></div>
    <p class="label__vintage">2009</p>
    <div class="label__rule label__rule--bottom"></div>
    <p class="label__type">Red Wine</p>
    <p class="label__volume">500ML</p>
    <p class="label__abv">11%Alcohol</p>
    <div class="label__band" role="img" aria-label="Strip of rust red painted canvas texture"></div>
  </section>

  <section class="label label--white">
    <div class="label__art">
      <div class="label__art-fill" role="img" aria-label="Abstract painted canvas texture in teal and deep green tones"></div>
      <h1 class="label__name">SipRoam</h1>
    </div>
    <div class="label__rule label__rule--top"></div>
    <p class="label__vintage">2009</p>
    <div class="label__rule label__rule--bottom"></div>
    <p class="label__type">White Wine</p>
    <p class="label__volume">500ML</p>
    <p class="label__abv">11%Alcohol</p>
    <div class="label__band" role="img" aria-label="Strip of teal painted canvas texture"></div>
  </section>
</body>
</html>
```